Social Media Marketing company needs a logo (tweak) and business card design

We need to slightly tidy up our logo, mainly to make sure we have the right design file (AI file type) also if possible remove the text below, for the business card we would like to get a fun yet professional feeling since we focus on social media marketing as well as event management
Target Market(s)
All industry really, just trying to look fun and professional to every one.
Industry/Entity Type
Marketing
Contact Information for Business Card
The Business Card needed to be fun yet professional
Font styles to use
Sans Serif
Colors
85cae6
Requirements
Must have
- The Logo.
- On the Name area, please provide two spaces 1. for English and Chinese.
- Rest is English only.
- Do not include a post code space.
- Phone number.
- Also please add website address www.brellavo.com
Nice to have
- Some water marks would be nice.
- Also the slogan "bright moves every day"

```html
<!DOCTYPE html>
<html lang="en">
<head>
<meta charset="utf-8">
<title>Brellavo Business Card</title>
<link href="https://fonts.googleapis.com/css2?family=Source+Sans+3:wght@400;600&family=Noto+Sans+SC:wght@500&display=swap" rel="stylesheet">
<style>
  :root {
    --backdrop: #e9e7e4;
    --card-light: #fbfbfa;
    --card-dark: #1c1c1d;
    --brand-blue: #85cae6;
    --brand-green: #7cc420;
    --ink: #3a3a3a;
    --ink-soft: #4a4a4a;
    --wordmark-light: #d8d8d8;
  }
  * { box-sizing: border-box; margin: 0; padding: 0; }
  html, body { width: 1200px; height: 844px; overflow: hidden; }
  body {
    background: var(--backdrop);
    font-family: "Source Sans 3", "Myriad Pro", sans-serif;
    position: relative;
  }
  .card {
    position: absolute;
    top: 272px;
    width: 520px;
    height: 300px;
    border-radius: 2px;
    box-shadow: 0 6px 18px rgba(0,0,0,0.12);
  }
  .card--front { left: 60px; background: var(--card-light); }
  .card--back  { left: 620px; background: var(--card-dark); }

  .brand {
    position: absolute;
    display: flex;
    align-items: center;
    gap: 12px;
  }
  .brand__dot {
    width: 30px; height: 30px;
    border-radius: 50%;
    background: var(--brand-blue);
  }
  .brand__name {
    font-size: 34px;
    font-weight: 400;
    letter-spacing: 0.2px;
    line-height: 40px;
  }
  .card--front .brand { right: 44px; top: 84px; }
  .card--front .brand__name { color: var(--ink); }

  .person { position: absolute; left: 44px; top: 138px; }
  .person__name { font-size: 21px; font-weight: 600; line-height: 24px; }
  .person__first { color: var(--brand-blue); }
  .person__last { color: var(--brand-green); }
  .person__name-zh {
    font-family: "Noto Sans SC", sans-serif;
    font-size: 15px; font-weight: 500; line-height: 20px;
    color: var(--ink);
  }
  .person__role { font-size: 14px; line-height: 18px; color: var(--ink-soft); }

  .contacts { position: absolute; left: 44px; top: 212px; list-style: none; }
  .contacts li {
    display: flex; align-items: center; gap: 12px;
    font-size: 15px; color: var(--ink); line-height: 22px;
  }
  .contacts svg { width: 12px; height: 12px; fill: var(--brand-blue); flex: none; }

  .card--back .brand {
    left: 0; right: 0; top: 112px;
    justify-content: center;
  }
  .card--back .brand__name { color: var(--wordmark-light); }
  .tagline {
    position: absolute; left: 0; right: 0; top: 162px;
    text-align: center;
    font-size: 16px; font-weight: 600;
    color: var(--brand-blue);
  }
</style>
</head>
<body>
  <section class="card card--front">
    <div class="brand">
      <span class="brand__dot"></span>
      <span class="brand__name">Brellavo</span>
    </div>
    <div class="person">
      <p class="person__name"><span class="person__first">Marcus</span> <span class="person__last">Lindqvist</span></p>
      <p class="person__name-zh" lang="zh">林马克</p>
      <p class="person__role">Managing Director</p>
    </div>
    <ul class="contacts">
      <li>
        <svg viewBox="0 0 12 12" aria-hidden="true"><path d="M2.4 0.6l2 2.2-1 1.3c.7 1.6 1.9 2.8 3.5 3.5l1.3-1 2.2 2-1.2 1.8C4.6 10.3 1.7 7.4.6 2.8z"/></svg>
        <span>(044)-318-2265</span>
      </li>
      <li>
        <svg viewBox="0 0 12 12" aria-hidden="true"><path d="M0 2h12v8H0z"/><path d="M1 3l5 3.8L11 3" fill="none" stroke="#fff" stroke-width="1"/></svg>
        <span>hello@brellavo.com</span>
      </li>
      <li>
        <svg viewBox="0 0 12 12" aria-hidden="true"><circle cx="6" cy="6" r="6"/><path d="M0.5 6h11M6 0.5c-2.4 3-2.4 8 0 11M6 0.5c2.4 3 2.4 8 0 11" fill="none" stroke="#fff" stroke-width="0.8"/></svg>
        <span>www.brellavo.com</span>
      </li>
    </ul>
  </section>

  <section class="card card--back">
    <div class="brand">
      <span class="brand__dot"></span>
      <span class="brand__name">Brellavo</span>
    </div>
    <p class="tagline">bright moves every day</p>
  </section>
</body>
</html>
```